Venlox - Property Management Company Listings - PSD / uncoded only

Our site simply connects property owners with property managers. I’m asking you to create 2 pages, 1 homepage and 1 page that lists of property management companies. Build with Responsive Design in mind. PSD/uncoded files only. Help us create a great site!
Example competitor sites:
http://www.everyestatehelp.example/
http://www.tendyourlots.example/
Inspired by these sites:
http://www.quorvik.example/
http://www.bespokely.example/
http://www.coinwire.example/
https://www.tripboard.example/
I've attached the logo as well as 2 picture files that you can consider using.
• Venlox Logo Colors: Yellow: HTML code: #FBC30A, RGB code: R: 251 G: 195 B: 10 Grey: HTML code: #4E4C4D, RGB code: R: 78 G: 76 B: 77
• The picture files are optional.
o One picture is of houses and neighborhood.
o The other is of a professional woman on the phone. Please do not use the professional woman as a large primary image. You can use the professional woman photo as a smaller photo and not the main photo.
• Please bring your own pictures and graphics too. Don't feel like you need to use mine.
Thank you!

```html
<!DOCTYPE html>
<html lang="en">
<head>
<meta charset="utf-8">
<title>Venlox – Find Your Local Property Manager</title>
<link href="https://fonts.googleapis.com/css2?family=Roboto:wght@300;400;500;700&display=swap" rel="stylesheet">
<style>
  :root {
    --brand-yellow: #fbc30a;
    --brand-grey: #4e4c4d;
    --header-bg: #f4f4f4;
    --steps-bg: #ececec;
    --features-bg: #f3f3f3;
    --cta-bg: #e6e6e6;
    --footer-bg: #555556;
    --blue: #1b8ef2;
    --text-dark: #333;
    --text-mid: #555;
    --icon-grey: #8a8a8a;
    --white: #fff;
  }
  * { box-sizing: border-box; margin: 0; padding: 0; }
  html, body { width: 840px; height: 1200px; overflow: hidden; }
  body { position: relative; font-family: 'Roboto', sans-serif; background: var(--white); color: var(--text-dark); }
  .abs { position: absolute; }

  /* Header */
  .site-header { left: 0; top: 0; width: 840px; height: 79px; background: var(--header-bg); }
  .brand { left: 65px; top: 18px; display: flex; align-items: center; gap: 8px; }
  .brand-mark { width: 12px; height: 12px; background: var(--brand-yellow); }
  .brand-name { font-size: 34px; font-weight: 700; color: var(--brand-grey); line-height: 1; }
  .tagline { left: 184px; top: 34px; width: 200px; font-size: 13px; line-height: 14px; color: #6d6d6d; }
  .main-nav { right: 64px; top: 39px; display: flex; gap: 18px; font-size: 13px; color: #444; }

  /* Hero */
  .hero { left: 0; top: 79px; width: 840px; height: 317px;
    background: linear-gradient(180deg, #5d6a62 0%, #7a6d62 35%, #8a7766 60%, #6d6e5c 100%); }
  .hero-title { left: 0; top: 133px; width: 840px; text-align: center; font-size: 26px; font-weight: 300; color: var(--white); letter-spacing: 0.5px; }
  .search-panel { left: 112px; top: 190px; width: 616px; height: 138px; background: rgba(40,45,50,0.35); border: 1px solid rgba(255,255,255,0.35); }
  .field { background: var(--white); height: 29px; font-size: 13px; color: #666; display: flex; align-items: center; padding-left: 20px; }
  .field-type { left: 149px; top: 210px; width: 240px; }
  .field-type svg { position: absolute; right: 6px; top: 6px; }
  .field-zip { left: 401px; top: 210px; width: 120px; color: #aaa; }
  .search-btn { left: 554px; top: 210px; width: 137px; height: 30px; background: var(--blue); color: var(--white); font-size: 14px; font-weight: 500; display: flex; align-items: center; justify-content: center; }
  .hero-note { left: 200px; top: 265px; width: 440px; text-align: center; font-size: 13px; line-height: 18px; color: var(--white); }

  /* Steps */
  .steps { left: 0; top: 396px; width: 840px; height: 276px; background: var(--steps-bg); border-bottom: 1px solid #dcdcdc; }
  .steps-title { left: 0; top: 430px; width: 840px; text-align: center; font-size: 23px; font-weight: 300; color: #333; }
  .step-card { top: 469px; height: 97px; background: var(--white); border: 1px solid #ddd; border-bottom: 4px solid var(--brand-yellow); display: flex; align-items: center; justify-content: center; }
  .step-caption { top: 586px; text-align: center; font-size: 15px; line-height: 19px; color: #222; letter-spacing: 0.3px; }

  /* Features */
  .features { left: 0; top: 672px; width: 840px; height: 346px; background: var(--features-bg); }
  .feature-list { left: 65px; top: 708px; width: 348px; height: 266px; background: var(--white); }
  .feature-row { position: absolute; left: 0; width: 348px; height: 89px; border-bottom: 1px solid #e2e2e2; }
  .feature-row svg.tab { position: absolute; left: 0; top: 0; }
  .feature-row p { position: absolute; left: 95px; top: 25px; width: 240px; font-size: 13px; line-height: 20px; color: #555; }
  .feature-photo { left: 424px; top: 708px; width: 352px; height: 266px;
    background: linear-gradient(120deg, #e8e4de 0%, #c9c3b8 40%, #6d6a66 70%, #2a2a2c 100%); }

  /* CTA */
  .cta { left: 0; top: 1018px; width: 840px; height: 98px; background: var(--cta-bg); border-top: 1px solid #d6d6d6; }
  .cta-title { left: 65px; top: 1039px; font-size: 20px; font-weight: 500; color: #333; }
  .cta-text { left: 65px; top: 1071px; font-size: 10px; line-height: 13px; color: #666; }
  .cta-btn { left: 533px; top: 1048px; width: 146px; height: 43px; background: var(--blue); color: var(--white); font-size: 15px; font-weight: 500; display: flex; align-items: center; justify-content: center; box-shadow: 0 2px 0 #0f6cc0; }

  /* Footer */
  .footer-rule { left: 0; top: 1116px; width: 840px; height: 5px; background: var(--brand-yellow); }
  .site-footer { left: 0; top: 1121px; width: 840px; height: 79px; background: var(--footer-bg); }
  .footer-nav { left: 0; top: 1141px; width: 840px; display: flex; justify-content: center; font-size: 11px; color: var(--white); }
  .footer-nav span { padding: 0 12px; border-left: 1px solid #888; }
  .footer-nav span:first-child { border-left: none; }
  .footer-divider { left: 65px; top: 1165px; width: 711px; height: 1px; background: #6a6a6a; }
  .copyright { left: 0; top: 1175px; width: 840px; text-align: center; font-size: 10px; color: #bbb; }
</style>
</head>
<body>
  <header class="site-header abs"></header>
  <div class="brand abs"><span class="brand-name">Venlox</span><span class="brand-mark"></span></div>
  <div class="tagline abs">Property Management Solutions Simplified</div>
  <nav class="main-nav abs"><span>HOME</span><span>ARE YOU A PROPERTY MANAGER?</span><span>CONTACT US</span></nav>

  <section class="hero abs" role="img" aria-label="Aerial photo of a suburban neighborhood with houses and trees"></section>
  <h1 class="hero-title abs">FIND YOUR LOCAL PROPERTY MANAGER</h1>
  <div class="search-panel abs"></div>
  <div class="field field-type abs">Select Your Property Type
    <svg width="17" height="17" viewBox="0 0 17 17"><circle cx="8.5" cy="8.5" r="8.5" fill="var(--brand-yellow)"/><path d="M5 7h7l-3.5 4z" fill="#333"/></svg>
  </div>
  <div class="field field-zip abs">In Zipcode</div>
  <div class="search-btn abs">SEARCH</div>
  <p class="hero-note abs">Search our directory to find experienced and professional property management companies that meet your needs.</p>

  <section class="steps abs"></section>
  <h2 class="steps-title abs">TO FIND PROPERTY MANAGEMENT COMPANIES NEAR YOU</h2>
  <div class="step-card abs" style="left:65px;width:229px">
    <svg width="40" height="40" viewBox="0 0 40 40" fill="var(--icon-grey)"><path d="M20 4 8 14h4v10h16V14h4z"/><path d="M4 26c6 0 10 2 14 4h10c2 0 2 3 0 3h-8v2h10l8-6c2-1 3 1 2 2l-9 8H4z"/></svg>
  </div>
  <div class="step-card abs" style="left:302px;width:232px">
    <svg width="58" height="40" viewBox="0 0 58 40" fill="var(--icon-grey)"><path d="M36 4 18 20h5v16h26V20h5z"/><circle cx="12" cy="18" r="5"/><path d="M3 36c0-8 4-12 9-12s9 4 9 12z"/><circle cx="24" cy="24" r="4"/><path d="M17 36c0-5 3-8 7-8s7 3 7 8z"/></svg>
  </div>
  <div class="step-card abs" style="left:545px;width:231px">
    <svg width="76" height="40" viewBox="0 0 76 40" fill="var(--icon-grey)"><circle cx="15" cy="11" r="6"/><path d="M2 36c0-10 5-15 13-15s13 5 13 15z"/><circle cx="38" cy="13" r="6"/><path d="M25 38c0-10 5-15 13-15s13 5 13 15z"/><circle cx="61" cy="11" r="6"/><path d="M48 36c0-10 5-15 13-15s13 5 13 15z"/></svg>
  </div>
  <p class="step-caption abs" style="left:65px;width:229px">Select your<br>property type and zipcode</p>
  <p class="step-caption abs" style="left:302px;width:232px">Review property<br>manager listings in your area</p>
  <p class="step-caption abs" style="left:545px;width:231px">Select and<br>compare property managers</p>

  <section class="features abs"></section>
  <div class="feature-list abs">
    <div class="feature-row" style="top:0">
      <svg class="tab" width="80" height="89" viewBox="0 0 80 89"><path d="M0 0h66l14 44.5L66 89H0z" fill="#3f3f40"/><g fill="var(--brand-yellow)"><path d="M33 30l-9 8h3v8h12v-8h3z"/><path d="M18 42l7 14h16l7-14-4 0-5 9H27l-5-9z"/></g></svg>
      <p>Making renting YOUR home an easy, stress-free experience.</p>
    </div>
    <div class="feature-row" style="top:89px">
      <svg class="tab" width="80" height="89" viewBox="0 0 80 89"><path d="M0 0h66l14 44.5L66 89H0z" fill="#3f3f40"/><path d="M14 38l8-5 8 3 6-3 8 2 6 4-4 3-10-3-4 2 8 6-3 3-9-6-4 3-7-3z" fill="var(--brand-yellow)"/></svg>
      <p>Connecting property owners with property managers.</p>
    </div>
    <div class="feature-row" style="top:178px">
      <svg class="tab" width="80" height="89" viewBox="0 0 80 89"><path d="M0 0h66l14 44.5L66 89H0z" fill="#3f3f40"/><g fill="var(--brand-yellow)"><circle cx="24" cy="30" r="4"/><path d="M19 36h10v22h-10z"/><path d="M38 40l-9 8h3v10h12V48h3z"/></g></svg>
      <p>Providing property management solutions, simplified.</p>
    </div>
  </div>
  <div class="feature-photo abs" role="img" aria-label="Photo of a professional property manager on the phone in a building corridor"></div>

  <section class="cta abs"></section>
  <h2 class="cta-title abs">ARE YOU A PROPERTY MANAGER?</h2>
  <p class="cta-text abs">Join our real estate property management company network.<br>Let us help you find leads of property owners seeking to rent their homes.</p>
  <div class="cta-btn abs">LEARN MORE</div>

  <div class="footer-rule abs"></div>
  <footer class="site-footer abs"></footer>
  <nav class="footer-nav abs"><span>Are you a Property Manager?</span><span>About Us</span><span>Contact Us</span><span>Terms of Use</span><span>Privacy Policy</span><span>Site Map</span></nav>
  <div class="footer-divider abs"></div>
  <p class="copyright abs">Copyright © 2014, Venlox, All Rights Reserved</p>
</body>
</html>
```